Physical Therapy Center for children Business Card

We need a Business Card for our company (Physical Therapy for children and youth with special needs) in Lisbon, Portugal. The name of the company is "Ninho de Luz"

The card must contain the following info:
- Logo: see uploaded file
- Name: Ninho de Luz
- Slogan: Plantamos carinho, vemos crescer, celebramos conquistas!
- Service: Terapias Especializadas
- Address: Rua Henrique Lobato Farinha 9C
- ZipCode: 2741-318 Vila Nova da Ribeira
- E-mail: geral@velado.pt
- Site: www.velado.pt
- Facebook: www.facebook.com/ninhodeluz
- Phone: +351 21 584 62 07
- Cell Phone: +351 96 731 84 25

The stationary should have contain all info from business card.

Target Market(s)

Parents of children with special needs

Industry/Entity Type

Physical Therapy

Contact Information for Business Card

The card design should be compatible with http://www.quellprensa.com/product2/order_detail.php?gid=40

Requirements
Should not have
• The business card should not have a Black background. Use white or other color.

```html
<!DOCTYPE html>
<html lang="pt">
<head>
<meta charset="utf-8">
<title>Ninho de Luz — Cartão de Visita</title>
<link rel="stylesheet" href="https://fonts.googleapis.com/css2?family=Questrial&family=Alegreya:ital@1&display=swap">
<style>
  :root {
    --ink: #3d3d3d;
    --red: #e8453c;
    --yellow: #f5cb22;
    --bar-yellow: #ffe600;
    --purple: #6e3766;
    --teal: #22b5a3;
    --paper: #ffffff;
    --frame: #1a1a1a;
  }
  * { margin: 0; padding: 0; box-sizing: border-box; }
  html, body { width: 1200px; height: 755px; overflow: hidden; background: var(--paper); }
  .card {
    position: relative;
    width: 1200px;
    height: 755px;
    background: var(--paper);
    border: 2px solid var(--frame);
    overflow: hidden;
    font-family: "Questrial", "Century Gothic", sans-serif;
    color: var(--ink);
  }
  .card-shapes { position: absolute; inset: 0; }
  .line { position: absolute; line-height: 1; white-space: nowrap; font-weight: 400; }

  .brand-mark {
    position: absolute; left: 300px; top: 110px;
    width: 104px; height: 104px; border-radius: 50%;
    background: var(--teal);
  }
  .brand-name { left: 0; width: 704px; text-align: center; top: 280px; font-size: 58px; letter-spacing: 2px; }
  .slogan {
    left: 92px; top: 331px; font-size: 24px;
    font-family: "Alegreya", Georgia, serif; font-style: italic; color: #222;
  }

  .web { left: 905px; top: 79px; font-size: 31px; }
  .dept { left: 778px; width: 347px; text-align: center; top: 172px; font-size: 42px; color: var(--purple); }
  .dept-bars { position: absolute; left: 778px; top: 228px; display: flex; gap: 14px; }
  .dept-bars span { display: block; width: 77px; height: 6px; }
  .bar-purple { background: var(--purple); }
  .bar-yellow { background: var(--bar-yellow); }
  .bar-red { background: var(--red); }
  .bar-teal { background: var(--teal); }

  .postal { right: 75px; text-align: right; font-size: 27px; }
  .postal-code { top: 269px; }
  .postal-town { top: 304px; }

  .contact { right: 77px; text-align: right; font-size: 34px; }
  .phone-land { top: 412px; }
  .phone-mobile { top: 452px; }
  .email { top: 493px; }
  .social { top: 531px; font-size: 33px; }

  .address { left: 653px; top: 644px; font-size: 32px; }
</style>
</head>
<body>
<main class="card">
  <svg class="card-shapes" width="1200" height="755" viewBox="0 0 1200 755" aria-hidden="true">
    <path class="band-yellow" d="M0 0 H36 C52 200 95 500 132 755 H0 Z" fill="var(--yellow)"/>
    <path class="wave-red" d="M88 359 C200 370 290 400 318 482 C370 600 470 720 612 755 H146 C130 620 110 470 88 359 Z" fill="var(--red)"/>

    <g class="icon-web">
      <circle cx="877" cy="94" r="14" fill="var(--red)"/>
      <rect x="869" y="87" width="16" height="10" rx="1.5" fill="none" stroke="#fff" stroke-width="2"/>
      <rect x="866" y="99" width="22" height="2.5" fill="#fff"/>
    </g>
    <g class="icon-phone" fill="#fff">
      <circle cx="807" cy="429" r="15" fill="var(--red)"/>
      <path d="M800 421 c2-2 4-1 5 1 l1 3 c0 2-2 2-2 3 c1 3 3 5 6 6 c1 0 1-2 3-2 l3 1 c2 1 3 3 1 5 c-2 2-5 3-9 1 c-5-3-8-6-10-11 c-1-3 0-5 2-7z"/>
    </g>
    <g class="icon-phone" fill="#fff">
      <circle cx="807" cy="469" r="15" fill="var(--red)"/>
      <path d="M800 461 c2-2 4-1 5 1 l1 3 c0 2-2 2-2 3 c1 3 3 5 6 6 c1 0 1-2 3-2 l3 1 c2 1 3 3 1 5 c-2 2-5 3-9 1 c-5-3-8-6-10-11 c-1-3 0-5 2-7z"/>
    </g>
    <g class="icon-mail">
      <circle cx="807" cy="510" r="15" fill="var(--red)"/>
      <rect x="798" y="503" width="18" height="13" fill="none" stroke="#fff" stroke-width="1.8"/>
      <path d="M798 503 L807 511 L816 503 M798 516 L804 509 M816 516 L810 509" fill="none" stroke="#fff" stroke-width="1.6"/>
    </g>
    <circle class="icon-social" cx="807" cy="548" r="15" fill="var(--red)"/>
    <g class="icon-pin">
      <circle cx="625" cy="660" r="15" fill="var(--red)"/>
      <path d="M625 670 C619 663 617 659 617 656 a8 8 0 0 1 16 0 c0 3-2 7-8 14z" fill="none" stroke="#fff" stroke-width="1.8"/>
      <circle cx="625" cy="656" r="2.6" fill="#fff"/>
    </g>
  </svg>

  <div class="brand-mark" aria-hidden="true"></div>
  <h1 class="line brand-name">NINHO DE LUZ</h1>
  <p class="line slogan">Plantamos carinho, vemos crescer, celebramos conquistas!</p>

  <p class="line web">www.velado.pt</p>
  <h2 class="line dept">GERAL</h2>
  <div class="dept-bars" aria-hidden="true">
    <span class="bar-purple"></span><span class="bar-yellow"></span><span class="bar-red"></span><span class="bar-teal"></span>
  </div>

  <p class="line postal postal-code">2741-318</p>
  <p class="line postal postal-town">Vila Nova da Ribeira</p>

  <p class="line contact phone-land">+351 21 584 62 07</p>
  <p class="line contact phone-mobile">+351 96 731 84 25</p>
  <p class="line contact email">geral@velado.pt</p>
  <p class="line contact social">/ninhodeluz</p>

  <p class="line address">Rua Henrique Lobato Farinha 9C</p>
</main>
</body>
</html>
```